Structural Engineering Firm Looking for High-Impact Lead Generation Focused Design (for B2B)

A well-established structural engineering firm in the UK wants a new website designed for them which will help them realise more business from online. Directly through the website as well as Ads and lead platforms. They need to compare favourably to competitors and have clarity. Current Site is here: http://www.quarlingpartners.example/ - you can take imagery from this site if you want to help with the design.

Target Market(s)

Homeowners, Architects, Designers, Construction Companies and Landlords

Industry/Entity Type

Professional Services

Number of Pages Required

5+ page

Font styles to use
Sans Serif

Requirements
Must have
• A Strong, Simple and Professional Design with a Focus on Lead Generation
Nice to have
• Creativity in the Detail, Clear Messaging
Should not have
• Too Much Colour, Too 'Consumer', Too Much Variation

```html
<!DOCTYPE html>
<html lang="en">
<head>
<meta charset="utf-8">
<title>Quarling Partners – Structural Engineering &amp; Party Wall Surveying</title>
<link href="https://fonts.googleapis.com/css2?family=Lato:wght@400;700;900&display=swap" rel="stylesheet">
<style>
:root{
  --coral:#e8705a;
  --ink:#222;
  --text:#555;
  --muted:#888;
  --teal:#a7cbc4;
  --beige:#ece2cb;
  --dark:#262626;
  --line:#ddd;
  --white:#fff;
}
*{box-sizing:border-box;margin:0;padding:0}
html,body{width:1200px;height:3848px;overflow:hidden}
body{font-family:'Lato',sans-serif;color:var(--text);background:var(--white);position:relative}
.wrap{width:800px;margin:0 auto;position:relative}
.btn{display:inline-block;background:var(--coral);color:var(--white);font-size:11px;font-weight:700;padding:9px 18px;border-radius:2px}
.btn-outline{display:inline-block;border:1px solid var(--white);color:var(--white);font-size:11px;padding:8px 18px}
h2{color:var(--ink);font-size:22px;font-weight:900;line-height:1.25}
p{font-size:12px;line-height:1.6}
.ph{display:block}

/* header */
.site-header{height:64px;position:relative;background:var(--white)}
.brand{position:absolute;left:200px;top:12px;font-weight:900;font-size:17px;line-height:18px;color:var(--ink);letter-spacing:1px;text-transform:uppercase}
.topbar{position:absolute;right:0;top:0;width:500px;height:20px;background:var(--coral);display:flex;gap:18px;justify-content:flex-end;padding-right:200px;align-items:center}
.topbar span{color:var(--white);font-size:10px}
.main-nav{position:absolute;right:200px;top:28px;display:flex;gap:18px;font-size:11px;font-weight:700;color:var(--ink)}
.main-nav .active{color:var(--coral);border-bottom:2px solid var(--coral);padding-bottom:4px}

/* hero */
.hero{height:496px;position:relative;background:linear-gradient(180deg,#3d4248 0%,#5a5c5c 45%,#2f2f2d 100%);text-align:center;color:var(--white)}
.hero h1{padding-top:170px;font-size:30px;font-weight:900;line-height:1.3}
.hero .lead{font-size:18px;margin-top:10px}
.quote-select{width:400px;margin:22px auto 0;height:40px;background:var(--white);display:flex;align-items:center;justify-content:space-between;padding-left:14px;color:var(--muted);font-size:12px}
.quote-select b{width:40px;height:40px;background:var(--coral);display:flex;align-items:center;justify-content:center}

/* intro */
.intro{height:680px;padding-top:60px}
.split{display:flex;justify-content:space-between;align-items:center}
.split .copy{width:360px}
.split .copy p{margin-top:14px}
.split .art{width:400px;height:250px}
.split+.split{margin-top:40px}

/* process */
.process{height:320px;background:var(--teal);padding-top:44px}
.process .head{display:flex;justify-content:space-between;align-items:flex-start}
.process .btn-outline{border-color:var(--coral);color:var(--ink);background:rgba(255,255,255,.2)}
.steps{display:flex;gap:8px;margin-top:26px}
.step{flex:1}
.step .ph{height:130px}
.step .tag{height:24px;background:var(--dark);color:var(--white);font-size:11px;font-weight:700;display:flex;align-items:center;justify-content:center}
.step .tag.alt{background:var(--coral)}

/* turnaround */
.turnaround{height:360px;padding-top:50px}
.turnaround .copy{width:320px}
.field{height:34px;border:1px solid var(--line);margin-top:16px;display:flex;align-items:center;justify-content:space-between;padding:0 12px;font-size:11px;color:var(--muted)}
.turnaround .btn{margin-top:16px}
.turnaround .art{width:440px;height:250px}

/* partnership */
.partnership{height:440px;background:linear-gradient(180deg,#4a4644,#3a3634);text-align:center;color:var(--white);padding-top:80px}
.partnership h2{color:var(--white);font-size:26px}
.partnership p{width:600px;margin:10px auto 0;font-size:11px}
.partnership .ask{margin-top:26px;font-size:13px;font-weight:700}
.partnership .btn-outline{margin-top:12px}

/* news */
.news{height:400px;background:var(--beige);padding-top:50px;text-align:center}
.news h2{font-size:20px}
.cards{display:flex;gap:20px;justify-content:center;margin-top:30px}
.card{width:200px;background:var(--white);text-align:center;padding-bottom:16px}
.card .ph{height:120px}
.card .date{color:var(--coral);font-size:10px;margin-top:10px}
.card h3{color:var(--ink);font-size:14px;font-weight:700;line-height:1.35;padding:6px 18px 0}

/* map */
.map{height:360px;background:linear-gradient(135deg,#e8eee5,#dce4e8)}

/* offices */
.offices{height:360px;padding-top:60px}
.offices .wrap{display:flex;justify-content:space-between}
.office{width:360px}
.office h2{font-size:18px}
.office dl{margin-top:16px;font-size:11px;line-height:1.6;color:var(--text)}
.office dt{font-weight:700;color:var(--ink);display:flex;align-items:center;gap:6px}
.office dd{margin-left:14px}
.office .phone{display:flex;align-items:center;gap:6px;margin-top:8px;font-size:11px}
.office .btn-line{display:inline-block;margin-top:14px;border:1px solid var(--coral);color:var(--coral);font-size:10px;padding:6px 12px}

/* footer */
.site-footer{height:368px;background:var(--dark);color:#bbb;position:relative}
.site-footer .wrap{display:flex;padding-top:40px}
.foot-brand{width:200px}
.foot-brand .brand-name{font-weight:900;font-size:17px;line-height:18px;color:var(--white);letter-spacing:1px;text-transform:uppercase}
.foot-brand p{font-size:10px;margin-top:16px;line-height:1.7}
.foot-col{width:170px;font-size:10px;line-height:1.8}
.foot-col h4{color:var(--white);font-size:12px;margin-bottom:4px}
.foot-col h4+h4,.foot-col span+h4{margin-top:8px}
.foot-col span{display:block}
.socials{position:absolute;left:200px;top:265px;display:flex;gap:6px}
.socials i{width:22px;height:22px;border:1px solid #777;display:block}
.socials i.on{background:var(--coral);border-color:var(--coral)}
.legal{position:absolute;left:0;right:0;bottom:0;height:40px;border-top:1px solid #3a3a3a}
.legal .wrap{display:flex;justify-content:space-between;align-items:center;height:40px;padding:0;font-size:10px;color:#999}
.legal .links{display:flex;gap:16px}
.mark{position:absolute;right:200px;top:45px;width:16px;height:16px;border:2px solid var(--coral)}
</style>
</head>
<body>

<header class="site-header">
  <div class="brand">Quarling<br>Partners</div>
  <div class="topbar"><span>Home</span><span>Blog</span><span>About Us</span><span>Contact Us</span></div>
  <nav class="main-nav">
    <span class="active">Home</span><span>Structural Design</span><span>Structural Surveys</span><span>Planning</span><span>Party Wall</span><span>Partners</span>
  </nav>
</header>

<section class="hero">
  <div role="img" aria-label="Evening photograph of a modern rendered house with lit windows" style="position:absolute;inset:0"></div>
  <h1 style="position:relative">Efficient &amp; Professional Structural Engineering<br>&amp; Party Wall Surveying</h1>
  <p class="lead" style="position:relative">Get a competitive quote from the local experts</p>
  <div class="quote-select" style="position:relative">What service are you looking for?
    <b><svg width="14" height="14" viewBox="0 0 14 14"><path d="M3 7h8M7 3l4 4-4 4" stroke="#fff" stroke-width="2" fill="none"/></svg></b>
  </div>
</section>

<section class="intro">
  <div class="wrap">
    <div class="split">
      <div class="copy">
        <h2>Structural engineers in london<br>and the south east</h2>
        <p>If you are looking for structural engineering services in the South East, then you should talk to our team. Whether a house extension, a loft conversion or major internal alterations to your property, we will design the structure you need and prepare it for approval.</p>
        <p>Operating across London and Sussex we work with homeowners, architects and contractors to provide a fast, friendly and fairly priced service.</p>
      </div>
      <div class="art ph" role="img" aria-label="Illustration of engineers assembling a building framework" style="background:linear-gradient(135deg,#f3d9a8,#c9d9ef)"></div>
    </div>
    <div class="split">
      <div class="art ph" role="img" aria-label="Illustration of an isometric building under construction" style="background:linear-gradient(135deg,#d6e3f3,#f5deb0)"></div>
      <div class="copy">
        <h2>Choose the party wall specialists</h2>
        <p>Where there is a wall, there is a way and we can help you and your neighbours reach agreement. Whether it is work on a shared wall, excavation near a boundary or a loft extension, we serve the right notices and prepare the awards.</p>
        <p>Our experienced surveyors act for building owners and adjoining owners alike, keeping projects moving and relations friendly from start to finish.</p>
        <p>Simply call +44 (0)20 7946 0321 or fill in the form and we will get back to you today.</p>
      </div>
    </div>
  </div>
</section>

<section class="process">
  <div class="wrap">
    <div class="head">
      <h2>From drawing to delivered<br>we support you every step of the way</h2>
      <span class="btn-outline">View Our Work</span>
    </div>
    <div class="steps">
      <div class="step"><div class="ph" role="img" aria-label="Photo of engineers reviewing plans" style="background:linear-gradient(135deg,#8c8f8a,#5e625f)"></div><div class="tag">Brief</div></div>
      <div class="step"><div class="ph" role="img" aria-label="Photo of technical drawings on a desk" style="background:linear-gradient(135deg,#c9b79a,#8a7a66)"></div><div class="tag alt">Design</div></div>
      <div class="step"><div class="ph" role="img" aria-label="Photo of a building site before works" style="background:linear-gradient(135deg,#9aa39a,#5f6a64)"></div><div class="tag">Before</div></div>
      <div class="step"><div class="ph" role="img" aria-label="Photo of a completed modern interior" style="background:linear-gradient(135deg,#d8d2c6,#9d968a)"></div><div class="tag alt">Delivery</div></div>
    </div>
  </div>
</section>

<section class="turnaround">
  <div class="wrap split">
    <div class="copy">
      <h2>Need a fast turnaround?</h2>
      <p>If your project is in the South East of England we can provide a fast turnaround if needed. Simply tell us the scope of the work and a member of our team will be in touch with a quote within one working day.</p>
      <div class="field">What service are you looking for?
        <svg width="10" height="6" viewBox="0 0 10 6"><path d="M1 1l4 4 4-4" stroke="#888" fill="none"/></svg>
      </div>
      <p style="margin-top:14px">The Quarling team will be on hand to help you through the process. From brief to sign-off, call us on +44 (0)20 7946 0321 to book a site visit.</p>
      <span class="btn">Book a Site Visit</span>
    </div>
    <div class="art ph" role="img" aria-label="Photo of a construction site with scaffolding and a crane" style="background:linear-gradient(160deg,#c7d6e4,#a39a8c 60%,#6d6559)"></div>
  </div>
</section>

<section class="partnership" style="position:relative">
  <div role="img" aria-label="Photo of a modern residential courtyard" style="position:absolute;inset:0"></div>
  <h2>We work in partnership</h2>
  <p>We are familiar in working closely with architects and building contractors on a wide range of projects so we are confident we can work with you.</p>
  <p class="ask">If you would like to explore partnering with Quarling</p>
  <span class="btn-outline">Partner With Us</span>
  <p class="ask">If you would like to explore partnering with Quarling</p>
  <span class="btn-outline">Introduce Us to Your Team</span>
</section>

<section class="news">
  <h2>News, Event &amp; Features</h2>
  <div class="cards">
    <article class="card"><div class="ph" role="img" aria-label="Photo of a bright kitchen extension" style="background:linear-gradient(135deg,#d9d3c8,#a39c90)"></div><div class="date">06 Jan 2022</div><h3>Lorem Ipsum is simply dummy text of the printing</h3></article>
    <article class="card"><div class="ph" role="img" aria-label="Photo of a row of townhouses" style="background:linear-gradient(135deg,#b8a693,#7e6f62)"></div><div class="date">20 Feb 2022</div><h3>Lorem Ipsum is simply dummy text of the printing</h3></article>
    <article class="card"><div class="ph" role="img" aria-label="Photo of a renovated interior" style="background:linear-gradient(135deg,#cfc9bd,#8f8a80)"></div><div class="date">10 Mar 2022</div><h3>Lorem Ipsum is simply dummy text of the printing</h3></article>
  </div>
</section>

<section class="map" role="img" aria-label="Street map of London and the South East with office location pins"></section>

<section class="offices">
  <div class="wrap">
    <div class="office">
      <h2>Quarling partners london</h2>
      <dl>
        <dt><svg width="8" height="11" viewBox="0 0 8 11"><path d="M4 0a4 4 0 0 0-4 4c0 3 4 7 4 7s4-4 4-7a4 4 0 0 0-4-4z" fill="#e8705a"/></svg>Main Office:</dt>
        <dd>Unit 4 Halden Yard<br>22 Merrow Street<br>London SE9 4QT<br>United Kingdom</dd>
      </dl>
      <div class="phone"><svg width="10" height="10" viewBox="0 0 10 10"><path d="M2 0l2 2-1 2c1 1 2 2 3 3l2-1 2 2-2 2C4 10 0 6 0 2z" fill="#e8705a"/></svg>+44 (0)20 7946 0321</div>
      <span class="btn-line">Contact Us</span>
    </div>
    <div class="office">
      <h2>Quarling partners sussex</h2>
      <dl>
        <dt><svg width="8" height="11" viewBox="0 0 8 11"><path d="M4 0a4 4 0 0 0-4 4c0 3 4 7 4 7s4-4 4-7a4 4 0 0 0-4-4z" fill="#e8705a"/></svg>Lewes:</dt>
        <dd>Studio 2 Fenwick House<br>15 Orchard Lane<br>Lewes BN7 9PL<br>United Kingdom</dd>
      </dl>
      <div class="phone"><svg width="10" height="10" viewBox="0 0 10 10"><path d="M2 0l2 2-1 2c1 1 2 2 3 3l2-1 2 2-2 2C4 10 0 6 0 2z" fill="#e8705a"/></svg>+44 (0)1632 960 418</div>
      <span class="btn-line">Contact Us</span>
    </div>
  </div>
</section>

<footer class="site-footer">
  <div class="wrap">
    <div class="foot-brand">
      <div class="brand-name">Quarling<br>Partners</div>
      <p>London<br>+44 (0)20 7946 0321<br>Sussex<br>+44 (0)1632 960 418</p>
    </div>
    <div class="foot-col">
      <h4>Design</h4>
      <span>House Extensions</span><span>Lofts</span><span>Alterations</span><span>Basements</span><span>Steel Frames</span><span>Temporary Works</span>
    </div>
    <div class="foot-col">
      <h4>Planning</h4>
      <span>Planning Applications</span><span>Planning Reports</span>
      <h4>Party Wall</h4>
      <span>Serving Party Wall Notices</span><span>Building Owner Surveyor</span><span>Adjoining Owner Surveyor</span><span>Schedules of Condition</span>
    </div>
    <div class="foot-col">
      <h4>Services</h4>
      <h4>Partners</h4>
      <h4>Gallery</h4>
      <h4>Blog</h4>
      <h4>About Us</h4>
      <h4>Contact Us</h4>
    </div>
  </div>
  <div class="mark"></div>
  <div class="socials"><i></i><i class="on"></i><i></i></div>
  <div class="legal"><div class="wrap"><span>© 2022 Quarling Partners. All Rights Reserved</span><span class="links"><span>Sitemap</span><span>Terms of Use</span><span>Privacy Policy</span><span>Cookies</span></span></div></div>
</footer>

</body>
</html>
```